Financial Service Company Need Business Card Design

This is a new startup company, first of its kind to offer this service. We facilitate the movement of deposit funds electronically between home buyers and real estate brokerages.Our customers are DOMIVANS®, real estate brokerages, and home buyers, we identify ourselves as a financial/technology company.
Not looking for anything too flashy. Just a clean design that shows the logo, contact info, etc. Company colors can be seen on attached logo, and 'coming soon page'
www.quorvanta.ca

```html
<!DOCTYPE html>
<html lang="en">
<head>
<meta charset="utf-8">
<title>Quorvanta — Business Card</title>
<link rel="stylesheet" href="https://fonts.googleapis.com/css2?family=Exo+2:wght@400;500;600&display=swap">
<style>
  :root {
    --page-bg: #e9e9ea;
    --card-top: #ffffff;
    --card-bottom: #e6e6e7;
    --ink-grey: #5f5f63;
    --ink-dark: #3a3a3d;
    --accent-orange: #f06a3b;
    --band-grey: #6b6b6e;
    --band-light: #c9c9cc;
  }
  * { margin: 0; padding: 0; box-sizing: border-box; }
  html, body {
    width: 1200px; height: 900px; overflow: hidden;
    background: var(--page-bg);
    font-family: "Exo 2", sans-serif;
  }
  .business-card {
    position: absolute; left: 100px; top: 164px;
    width: 1000px; height: 571px;
    border-radius: 56px; overflow: hidden;
    background: radial-gradient(ellipse at 60% 35%, var(--card-top) 0%, var(--card-bottom) 100%);
    box-shadow: 0 18px 40px rgba(0,0,0,0.18);
  }
  .card-waves { position: absolute; inset: 0; width: 100%; height: 100%; }
  .brand {
    position: absolute; left: 70px; top: 58px;
    display: flex; align-items: center; gap: 24px;
  }
  .brand-square { width: 58px; height: 58px; background: var(--accent-orange); }
  .brand-name {
    font-size: 84px; font-weight: 500; color: var(--ink-grey);
    line-height: 1; letter-spacing: 0.5px;
  }
  .contact-list {
    position: absolute; left: 62px; top: 200px;
    list-style: none;
  }
  .contact-item {
    display: flex; align-items: center; gap: 16px;
    height: 42px; font-size: 23px; color: var(--ink-dark); letter-spacing: 1px;
  }
  .contact-item svg { width: 22px; height: 22px; fill: var(--accent-orange); flex: none; }
  .contact-item.small { font-size: 20px; letter-spacing: 0.5px; }
  .person {
    position: absolute; right: 110px; top: 368px; text-align: right;
  }
  .person-name {
    font-size: 30px; font-weight: 500; color: var(--accent-orange);
    letter-spacing: 2px; text-transform: uppercase;
  }
  .person-title {
    font-size: 20px; font-weight: 500; color: var(--ink-dark);
    letter-spacing: 2px; text-transform: uppercase; margin-top: 4px;
  }
</style>
</head>
<body>
  <article class="business-card">
    <svg class="card-waves" viewBox="0 0 1000 571" preserveAspectRatio="none" aria-hidden="true">
      <path d="M0,440 C250,520 620,540 1000,420 L1000,571 L0,571 Z" fill="var(--band-grey)"/>
      <path d="M0,410 C250,490 620,515 1000,400 L1000,420 C620,540 250,520 0,440 Z" fill="var(--band-light)"/>
      <path d="M0,385 C220,470 460,500 640,492" fill="none" stroke="var(--accent-orange)" stroke-width="7"/>
      <path d="M620,492 C800,478 910,440 1000,372 L1000,400 C900,460 790,490 620,492 Z" fill="var(--accent-orange)"/>
    </svg>

    <div class="brand">
      <span class="brand-square"></span>
      <span class="brand-name">Quorvanta</span>
    </div>

    <ul class="contact-list">
      <li class="contact-item">
        <svg viewBox="0 0 24 24"><path d="M6.6 10.8a15.1 15.1 0 0 0 6.6 6.6l2.2-2.2c.3-.3.7-.4 1-.2 1.1.4 2.3.6 3.6.6.6 0 1 .4 1 1V20c0 .6-.4 1-1 1A17 17 0 0 1 3 4c0-.6.4-1 1-1h3.5c.6 0 1 .4 1 1 0 1.3.2 2.5.6 3.6.1.3 0 .7-.2 1z"/></svg>
        <span>014 562 3890</span>
      </li>
      <li class="contact-item">
        <svg viewBox="0 0 24 24"><path d="M7 1h10a2 2 0 0 1 2 2v18a2 2 0 0 1-2 2H7a2 2 0 0 1-2-2V3a2 2 0 0 1 2-2zm0 3v15h10V4zm5 16.2a1 1 0 1 0 0 .1z"/></svg>
        <span>014 562 3891</span>
      </li>
      <li class="contact-item">
        <svg viewBox="0 0 24 24"><path d="M6 2h9l3 3v5h1a3 3 0 0 1 3 3v8H2v-8a3 3 0 0 1 3-3h1zm2 2v6h8V6h-2V4zm-2 10v2h12v-2z"/></svg>
        <span>014 562 3892</span>
      </li>
      <li class="contact-item small">
        <svg viewBox="0 0 24 24"><path d="M2 5h20v14H2zm2 2v.5l8 5 8-5V7zm0 3v7h16v-7l-8 5z"/></svg>
        <span>dan@quorvanta.ca</span>
      </li>
      <li class="contact-item small">
        <svg viewBox="0 0 24 24"><path d="M12 2a10 10 0 1 0 0 20 10 10 0 0 0 0-20zm6.9 6h-3a15 15 0 0 0-1.3-3.9A8 8 0 0 1 18.9 8zM12 4c.8 1.2 1.5 2.5 1.9 4h-3.8c.4-1.5 1.1-2.8 1.9-4zM4.3 14a8 8 0 0 1 0-4h3.3a16 16 0 0 0 0 4zm.8 2h3a15 15 0 0 0 1.3 3.9A8 8 0 0 1 5.1 16zm3-8h-3a8 8 0 0 1 4.3-3.9A15 15 0 0 0 8.1 8zM12 20c-.8-1.2-1.5-2.5-1.9-4h3.8c-.4 1.5-1.1 2.8-1.9 4zm2.3-6H9.7a14 14 0 0 1 0-4h4.6a14 14 0 0 1 0 4zm.3 5.9a15 15 0 0 0 1.3-3.9h3a8 8 0 0 1-4.3 3.9zm1.8-5.9a16 16 0 0 0 0-4h3.3a8 8 0 0 1 0 4z"/></svg>
        <span>www.quorvanta.ca</span>
      </li>
    </ul>

    <div class="person">
      <p class="person-name">Daniel Revick</p>
      <p class="person-title">Financial Advisor</p>
    </div>
  </article>
</body>
</html>
```